Dental Website offering Continuing Educational Courses

Need a Wordpress CMS design for a dentist website which will offer continuing education courses. The design should be professional, simple and elegant. Logo versions are provided. Please follow those colors plus one or two others that will blend well. Here's examples of other sites they like - www.pelvaronix.com, www.qortiva.com, www.thebriselmoreinstitute.com., www.kwjt.org/. Please provide designs in jpg format. If selected, then final design will be required in psd format.

Target Market(s)

dentists, endodontists (root canal specialists)

Industry/Entity Type

Education

Requirements
Must have
• Combination Horizontal / Vertical navigation. Place course titles in vertical nav in a side bar on home page. List them as Course 1, Course 2 ,etc.. total of 7 courses. The header horizontal nav should be; Home, About, Courses, Doctor Name, Faculty, FAQ, Patients, Contact.
Need placeholder to accommodate one large static image just under main nav. Need web safe fonts. Need placeholder for calendar like this example www.tumbledfields.org/. Need to show a dropdown menu example. Design for 1024 x 768. Need space on home page to allow for logos of external websites/ associations. These are; www.fennicoralbo.com, www.yarplova.com, www.hmu.org/, www.corvintagha.com/corv/. Would like to see a row of images across the bottom of the home page like the www.kwjt.org site has. Would like to show a Contact Form on the home page like the "need assistance" form example on www.thebriselmoreinstitute.com. Would like to create a placeholder on the home page for an image of a doctor.
Nice to have
• 3 or 4 column footer (which features sitemap, copyright, etc..). Examples in the design for the web site’s copy styling:
o through headers
o Bulleted list
o Hyperlink
o Table

```html
<!DOCTYPE html>
<html lang="en">
<head>
<meta charset="utf-8">
<title>Yarplova – Continuing Dental Education</title>
<link rel="stylesheet" href="https://fonts.googleapis.com/css2?family=EB+Garamond:wght@400;600&family=PT+Sans:wght@400;700&display=swap">
<style>
:root{
  --page-bg:#e8edf1;
  --nav-blue:#0a4d96;
  --header-blue:#0b4f98;
  --drop-blue:#1b6fd0;
  --side-blue:#0c4f99;
  --side-active:#07356a;
  --flyout:#0d3f7a;
  --ink:#2b2b2b;
  --muted:#8a8a8a;
  --head-blue:#0b5aa6;
  --rule:#e3e6ea;
  --green:#6f9a2c;
  --footer-deep:#0a3562;
  --footer-col:#1a66c2;
  --footer-panel:#0e4f9f;
  --footer-bar:#0b3a70;
  --footer-text:#a9c6ea;
}
*{box-sizing:border-box;margin:0;padding:0}
html,body{width:1050px;height:1200px;overflow:hidden}
body{background:var(--page-bg);font-family:Arial,Helvetica,sans-serif;color:var(--ink);position:relative}
.abs{position:absolute}
.footer-band{left:0;top:957px;width:1050px;height:243px;background:var(--footer-deep)}
.column{left:151px;top:0;width:751px;height:957px;background:#fff}
.column-foot{left:151px;top:957px;width:751px;height:243px;background:var(--footer-col)}
.top-strip{left:151px;top:0;width:751px;height:6px;background:#4a4f56}

/* main navigation */
.main-nav{left:151px;top:6px;width:751px;height:31px;background:var(--nav-blue)}
.main-nav a{position:absolute;top:7px;color:#fff;font:700 12px Arial,sans-serif;text-decoration:none;transform:translateX(-50%);letter-spacing:.3px}
.dropdown{left:336px;top:37px;width:102px;height:98px;background:var(--drop-blue);padding:5px 0 0 23px}
.dropdown a{display:block;color:#fff;font:700 10px Arial,sans-serif;line-height:18.5px;text-decoration:none}
.dropdown a.current{text-decoration:underline}

/* header */
.masthead{left:161px;top:47px;width:730px;height:88px;background:var(--header-blue)}
.brand{left:174px;top:64px;display:flex;align-items:center;gap:8px}
.brand-mark{width:14px;height:14px;background:#fff}
.brand-name{color:#fff;font:700 24px "PT Sans",sans-serif}
.brand-tag{left:174px;top:97px;width:150px;color:#fff;font:400 10px "PT Sans",sans-serif;letter-spacing:.4px;white-space:nowrap}
.inquiry{right:167px;top:72px;text-align:right;color:#fff;font-family:"EB Garamond",serif}
.inquiry small{display:block;font-size:13px;letter-spacing:.5px}
.inquiry strong{display:block;font-size:31px;font-weight:400;line-height:30px}

/* hero */
.course-nav{left:161px;top:145px;width:154px;height:218px;background:var(--side-blue)}
.course-nav a,.flyout a{display:flex;align-items:center;height:23.3px;color:#cfe0f5;font:400 15px Arial,sans-serif;text-decoration:none;padding-left:14px}
.course-nav a svg,.flyout a svg{margin-right:14px}
.course-nav a.current{background:var(--side-active);color:#fff}
.flyout{left:315px;top:172px;width:125px;height:131px;background:var(--flyout);padding-top:4px}
.flyout a.current{background:#0a4d96;color:#fff;margin:0 5px}
.hero-image{left:315px;top:145px;width:576px;height:218px;background:linear-gradient(90deg,#f3b88a 0%,#e9a06b 30%,#d98550 55%,#c98a66 75%,#8d7b6b 100%)}

/* welcome */
.section-title{font:400 22px "PT Sans",sans-serif;color:var(--head-blue)}
.welcome-title{left:161px;top:376px}
.welcome-copy{left:161px;top:403px;width:306px;font-size:8.4px;line-height:14.5px;color:var(--muted)}
.read-more{left:391px;top:486px;width:72px;height:22px;background:#f1f3f5;border:1px solid #d8dde2;border-radius:3px;font:700 9.5px Arial,sans-serif;color:var(--head-blue);display:flex;align-items:center;justify-content:center;gap:5px}
.doctor-photo{left:480px;top:394px;width:165px;height:111px;border:3px solid #fff;box-shadow:0 1px 4px rgba(0,0,0,.35);background:linear-gradient(90deg,#4a6fa8 0%,#b8c6d6 45%,#eef0f2 100%)}

.divider-v{left:660px;top:370px;width:1px;height:446px;background:var(--rule)}

/* calendar */
.calendar{left:690px;top:383px;width:180px}
.cal-head{height:27px;background:linear-gradient(#3c3f44,#1f2124);color:#fff;font:700 11px Arial,sans-serif;border-radius:4px 4px 0 0;display:flex;align-items:center;justify-content:space-between;padding:0 10px}
.calendar table{width:100%;border-collapse:collapse}
.calendar th{font:400 7.5px Arial,sans-serif;color:#888;height:13px;background:#f3f4f5}
.calendar td{height:25.5px;text-align:center;font:700 10px Arial,sans-serif;color:#333;border:1px solid #fff;background:#e7e8ea}
.calendar td.off{color:#b5b5b5;background:#eeeff0}
.calendar td.today{background:#4b4e53;color:#fff}
.calendar td.event{background:#d9dadc}

/* contact form */
.assist{left:674px;top:573px;width:211px;height:243px;border:1px solid #dde2e7;border-radius:3px}
.assist h3{font:400 16px "EB Garamond",serif;color:var(--head-blue);padding:4px 0 0 12px;height:26px;border-bottom:1px solid #e3e6ea;background:linear-gradient(#fff,#f4f6f8)}
.field{position:absolute;left:12px;font-size:9.5px;color:#444}
.input{position:absolute;left:60px;width:143px;height:18px;border:1px solid #dfe3e7}
.submit{left:799px;top:776px;width:70px;height:21px;background:linear-gradient(#8bb33d,#5f8a23);border-radius:3px;color:#fff;font:700 9px Arial,sans-serif;display:flex;align-items:center;justify-content:center}

/* doctors */
.doctors-title{left:164px;top:521px;font-size:17px}
.rule-h{height:1px;background:var(--rule)}
.doctor-card{top:558px;width:81px;height:66px;border:1px solid #cfd4d9;padding:3px;background:#fff;box-shadow:1px 2px 3px rgba(0,0,0,.2)}
.doctor-card div{width:100%;height:100%;background:linear-gradient(#c9ced3,#e8eaec 60%,#fff)}
.doctor-name{top:629px;width:81px;text-align:center;font-size:10.5px;color:#aaa}
.doctor-name.current{color:var(--head-blue)}

/* testimonial & news */
.card{top:664px;width:211px;height:150px;border:1px solid #dde2e7;border-radius:3px}
.card h3{font:600 15.5px "EB Garamond",serif;color:var(--head-blue);height:26px;padding:2px 0 0 10px;background:linear-gradient(#fff,#eef2f6);border-bottom:1px solid #e3e6ea}
.student-photo{left:178px;top:699px;width:67px;height:73px;background:linear-gradient(#f5d99a,#ecc8a8 60%,#e6e6e6)}
.quote{left:256px;top:699px;width:125px;font:italic 12px/16.5px "EB Garamond",serif;color:#333}
.quote-by{left:188px;top:779px;font:700 8.5px/11px Arial,sans-serif;color:#333}
.news-thumb{left:426px;width:64px;height:45px;background:linear-gradient(#b65a52,#e8b0a6 50%,#f3e7e1)}
.news-text{left:499px;width:125px;font-size:8px;line-height:12.5px;color:var(--muted)}

/* partner links */
.links-band{left:167px;top:834px;width:719px;height:107px;border:1px solid #cfd6dd}
.links-tab{left:168px;top:838px;width:29px;height:94px;background:var(--green)}
.links-tab span{position:absolute;left:4px;top:70px;transform:rotate(-90deg);transform-origin:left top;color:#fff;font:400 14px "EB Garamond",serif;letter-spacing:2px;white-space:nowrap}
.partner{top:852px;display:flex;flex-direction:column;align-items:center;gap:8px;font:400 12px "PT Sans",sans-serif;color:#1b1b1b;text-align:center}
.partner-mark{width:40px;height:40px;background:#1f2a33}

/* footer */
.footer-panel{left:166px;top:978px;width:720px;height:116px;background:var(--footer-panel);border:1px solid #2f74c9;border-radius:4px}
.footer-col{top:990px;font-size:9.5px;line-height:15.5px;color:var(--footer-text)}
.footer-col h4{font:700 10px Arial,sans-serif;color:#fff;margin-bottom:14px}
.social{width:22px;height:22px;border-radius:50%;background:#cfdff2}
.footer-bar{left:185px;top:1094px;width:688px;height:40px;background:var(--footer-bar)}
.footer-bar nav{display:flex;justify-content:center;align-items:center;height:26px;gap:18px;font-size:9.5px;color:#cfe0f5}
.copyright{left:151px;top:1147px;width:751px;text-align:center;font-size:9px;color:#cfe0f5}
</style>
</head>
<body>
<div class="abs footer-band"></div>
<div class="abs column"></div>
<div class="abs column-foot"></div>
<div class="abs top-strip"></div>

<nav class="abs main-nav">
  <a href="#" style="left:48px">HOME</a>
  <a href="#" style="left:134px">ABOUT</a>
  <a href="#" style="left:238px">COURSES</a>
  <a href="#" style="left:359px">DOCTOR NAME</a>
  <a href="#" style="left:486px">FACULTY</a>
  <a href="#" style="left:578px">FAQ</a>
  <a href="#" style="left:667px">CONTACT</a>
</nav>

<header class="abs masthead"></header>
<div class="abs brand"><span class="brand-mark"></span><span class="brand-name">Yarplova</span></div>
<div class="abs brand-tag">CONTINUING DENTAL EDUCATION</div>
<div class="abs inquiry"><small>CALL FOR INQUIRIES!</small><strong>123 456 7890</strong></div>

<div class="abs dropdown">
  <a href="#">Course 1</a><a href="#" class="current">Course 2</a><a href="#">Course 3</a><a href="#">Course 4</a><a href="#">Course 5</a>
</div>

<div class="abs hero-image" role="img" aria-label="Row of smiling dental students"></div>
<nav class="abs course-nav">
  <a href="#"><svg width="6" height="8" viewBox="0 0 6 8"><path d="M1 1l3 3-3 3" stroke="#fff" stroke-width="1.6" fill="none"/></svg>Course 1</a>
  <a href="#" class="current"><svg width="6" height="8" viewBox="0 0 6 8"><path d="M1 1l3 3-3 3" stroke="#fff" stroke-width="1.6" fill="none"/></svg>Course 2</a>
  <a href="#"><svg width="6" height="8" viewBox="0 0 6 8"><path d="M1 1l3 3-3 3" stroke="#fff" stroke-width="1.6" fill="none"/></svg>Course 3</a>
  <a href="#"><svg width="6" height="8" viewBox="0 0 6 8"><path d="M1 1l3 3-3 3" stroke="#fff" stroke-width="1.6" fill="none"/></svg>Course 4</a>
  <a href="#"><svg width="6" height="8" viewBox="0 0 6 8"><path d="M1 1l3 3-3 3" stroke="#fff" stroke-width="1.6" fill="none"/></svg>Course 5</a>
  <a href="#"><svg width="6" height="8" viewBox="0 0 6 8"><path d="M1 1l3 3-3 3" stroke="#fff" stroke-width="1.6" fill="none"/></svg>Course 6</a>
  <a href="#"><svg width="6" height="8" viewBox="0 0 6 8"><path d="M1 1l3 3-3 3" stroke="#fff" stroke-width="1.6" fill="none"/></svg>Course 7</a>
  <a href="#"><svg width="6" height="8" viewBox="0 0 6 8"><path d="M1 1l3 3-3 3" stroke="#fff" stroke-width="1.6" fill="none"/></svg>Course 8</a>
  <a href="#"><svg width="6" height="8" viewBox="0 0 6 8"><path d="M1 1l3 3-3 3" stroke="#fff" stroke-width="1.6" fill="none"/></svg>Course 9</a>
</nav>
<nav class="abs flyout">
  <a href="#"><svg width="6" height="8" viewBox="0 0 6 8"><path d="M1 1l3 3-3 3" stroke="#fff" stroke-width="1.6" fill="none"/></svg>Course 1</a>
  <a href="#" class="current"><svg width="6" height="8" viewBox="0 0 6 8"><path d="M1 1l3 3-3 3" stroke="#fff" stroke-width="1.6" fill="none"/></svg>Course 2</a>
  <a href="#"><svg width="6" height="8" viewBox="0 0 6 8"><path d="M1 1l3 3-3 3" stroke="#fff" stroke-width="1.6" fill="none"/></svg>Course 3</a>
  <a href="#"><svg width="6" height="8" viewBox="0 0 6 8"><path d="M1 1l3 3-3 3" stroke="#fff" stroke-width="1.6" fill="none"/></svg>Course 4</a>
  <a href="#"><svg width="6" height="8" viewBox="0 0 6 8"><path d="M1 1l3 3-3 3" stroke="#fff" stroke-width="1.6" fill="none"/></svg>Course 5</a>
</nav>

<h2 class="abs section-title welcome-title">WELCOME</h2>
<p class="abs welcome-copy">Lorem ipsum dolor sit amet, consectetuer adipiscing elit. Aeneacommodo ligula eget dolor.Lorem ipsum dolor sit amet, consectetuer adipiscing elit. AenLorem ipsum dolor sitmet, consectetuer adipiscing elit. ean commodo ligula eget dolor.ean commodo ligulat dolor.Loreor sit amet, consectetuer adipiscing elit. Aenean commodo ligulegLoremet, consectetuer adipiscing elit. Aenean commodo ligula eget doLorem ipsum</p>
<div class="abs read-more">Read more <svg width="6" height="8" viewBox="0 0 6 8"><path d="M1 1l3 3-3 3" stroke="#0b5aa6" stroke-width="1.8" fill="none"/></svg></div>
<div class="abs doctor-photo" role="img" aria-label="Dentist examining a young patient"></div>

<div class="abs divider-v"></div>

<div class="abs calendar">
  <div class="cal-head"><span>◂</span><span>April 2011</span><span>▸</span></div>
  <table>
    <tr><th>MON</th><th>TUE</th><th>WED</th><th>THU</th><th>FRI</th><th>SAT</th><th>SUN</th></tr>
    <tr><td class="off">28</td><td class="off">29</td><td class="off">30</td><td class="off">31</td><td>1</td><td>2</td><td>3</td></tr>
    <tr><td class="today">4</td><td>5</td><td class="event">6</td><td>7</td><td>8</td><td>9</td><td>10</td></tr>
    <tr><td>11</td><td>12</td><td>13</td><td>14</td><td>15</td><td>16</td><td>17</td></tr>
    <tr><td>18</td><td>19</td><td>20</td><td>21</td><td>22</td><td>23</td><td>24</td></tr>
    <tr><td>25</td><td>26</td><td>27</td><td>28</td><td>29</td><td>30</td><td class="off">1</td></tr>
  </table>
</div>

<form class="abs assist">
  <h3>Need Assistance?</h3>
  <span class="field" style="top:38px">Name</span><span class="input" style="top:34px"></span>
  <span class="field" style="top:62px">email ID</span><span class="input" style="top:58px"></span>
  <span class="field" style="top:86px">phone no</span><span class="input" style="top:82px"></span>
  <span class="field" style="top:110px">Address</span><span class="input" style="top:106px"></span>
  <span class="field" style="top:134px">Messagebox</span>
  <span class="input" style="top:150px;left:12px;width:191px;height:50px"></span>
</form>
<div class="abs submit">Submit</div>

<h2 class="abs section-title doctors-title">OUR DOCTORS</h2>
<div class="abs rule-h" style="left:161px;top:547px;width:490px"></div>
<div class="abs doctor-card" style="left:202px"><div role="img" aria-label="Portrait of a doctor"></div></div>
<div class="abs doctor-card" style="left:314px"><div role="img" aria-label="Portrait of a doctor"></div></div>
<div class="abs doctor-card" style="left:424px"><div role="img" aria-label="Portrait of a doctor"></div></div>
<div class="abs doctor-card" style="left:536px"><div role="img" aria-label="Portrait of a doctor"></div></div>
<div class="abs doctor-name current" style="left:202px">NAME</div>
<div class="abs doctor-name" style="left:314px">NAME</div>
<div class="abs doctor-name" style="left:424px">NAME</div>
<div class="abs doctor-name" style="left:536px">NAME</div>
<div class="abs rule-h" style="left:161px;top:648px;width:490px"></div>

<section class="abs card" style="left:171px"><h3>Testimonials</h3></section>
<div class="abs student-photo" role="img" aria-label="Portrait of a student"></div>
<p class="abs quote">Lorem ipsum dolor siamet, consectetuer g elit. Aenean commodo ligula eget dolor. Aenean masula eget dolor. Aenean massa. Cum sociis natoque"</p>
<p class="abs quote-by">- MERIN<br>&nbsp;&nbsp;student</p>

<section class="abs card" style="left:419px"><h3>News &amp; Events</h3></section>
<div class="abs news-thumb" style="top:698px" role="img" aria-label="Close-up of a smile"></div>
<p class="abs news-text" style="top:700px">Lorem ipsum dolor sit amet, consectetuer adipiscing elit. Aenean commodo ligula eget dolor.</p>
<div class="abs news-thumb" style="top:757px" role="img" aria-label="Close-up of a smile"></div>
<p class="abs news-text" style="top:759px">Lorem ipsum dolor sit amet, consectetuer adipiscing elit. Aenean commodo ligula eget dolor.</p>

<div class="abs links-band"></div>
<div class="abs links-tab"><span>LINKS</span></div>
<div class="abs partner" style="left:222px;width:120px"><span class="partner-mark"></span>Halvern Dental Guild</div>
<div class="abs partner" style="left:355px;top:876px;width:190px;flex-direction:row;gap:6px"><span class="partner-mark" style="width:14px;height:14px;background:#3a7bd5"></span>Corvintagha Endo</div>
<div class="abs partner" style="left:594px;top:866px;width:165px;height:30px;background:#2a2a2a;color:#fff;justify-content:center">The Briselmore Institute</div>
<div class="abs partner" style="left:752px;width:120px"><span class="partner-mark"></span>Halvern Dental Guild</div>

<footer>
  <div class="abs footer-panel"></div>
  <div class="abs footer-col" style="left:198px"><h4>Company</h4>About us<br>Vision<br>Team<br>Success Stories</div>
  <div class="abs footer-col" style="left:325px"><h4>Student</h4>Tests<br>Educational Loans<br>Faqs</div>
  <div class="abs footer-col" style="left:455px"><h4>Why us</h4>Why Choose Us<br>Testimonials<br>Press Clips<br>Photo Gallery</div>
  <div class="abs footer-col" style="left:579px"><h4>Online</h4>Enquiry<br>Registration<br>Feedback</div>
  <div class="abs footer-col" style="left:680px;width:100px"><h4>Contacts</h4>Lorem ipsum dolor sit amet, consectetuer adipiscing elit. Aenean commodo</div>
  <div class="abs footer-col" style="left:796px"><h4>Follow Us</h4></div>
  <span class="abs social" style="left:791px;top:1016px"></span>
  <span class="abs social" style="left:825px;top:1016px"></span>
  <span class="abs social" style="left:791px;top:1052px"></span>
  <span class="abs social" style="left:825px;top:1052px"></span>
  <div class="abs footer-bar">
    <nav><span>Home</span>|<span>About</span>|<span>Courses</span>|<span>Doctor Name</span>|<span>Faculty</span>|<span>FAQ</span>|<span>Patients</span>|<span>Contact</span></nav>
  </div>
  <p class="abs copyright">Dental Website – Copyright © 2012</p>
</footer>
</body>
</html>
```